Brivet Networks, Inc. Website redesign

Revamp the website, it is old and outdated. www.brivetnetworksinc.com

Target Market(s)

Information Technology Consulting and Staffing

Coding

Coded - Design and coding required

Number of Pages Required

5+ page

Colors

Designer to choose colors to be used in the design.

Requirements
Must have
• Outlined text boxes just like from the Hollis.us site. A clean look

```html
<!DOCTYPE html>
<html lang="en">
<head>
<meta charset="utf-8">
<title>Brivet Networks – Our services</title>
<link href="https://fonts.googleapis.com/css2?family=Open+Sans:wght@300;400;600;700&display=swap" rel="stylesheet">
<style>
:root{
  --ink:#212529;
  --muted:#6c757d;
  --brand-red:#9b1c2e;
  --header-bg:#f7f7f9;
  --hero-bg:#f5f5f6;
  --section-bg:#e9ecef;
  --card-bg:#ffffff;
  --card-border:#dfe2e6;
  --link:#1a73e8;
}
*{box-sizing:border-box;margin:0;padding:0}
html,body{width:1200px;height:956px;overflow:hidden}
body{font-family:"Open Sans",sans-serif;color:var(--ink);background:var(--hero-bg);font-size:9.4px;line-height:15px}
.site-header{height:67px;display:flex;align-items:center;padding:0 15px 0 20px;background:var(--header-bg)}
.brand{display:flex;align-items:center;gap:8px}
.brand-mark{width:12px;height:12px;background:var(--brand-red)}
.brand-name{font-weight:700;font-size:20px;letter-spacing:.5px;color:var(--ink)}
.tagline{margin-left:24px;font-weight:300;font-size:17px;color:#444;letter-spacing:.3px}
.main-nav{margin-left:auto;display:flex;gap:10px;font-size:9.4px}
.main-nav a{color:var(--muted);text-decoration:none}
.main-nav a.active{color:var(--ink)}
.hero{height:153px;padding-top:18px}
.hero h1{text-align:center;font-weight:600;font-size:25px;line-height:30px}
.hero .inner{width:694px;margin:0 auto}
.hero h2{font-weight:600;font-size:18px;line-height:22px;margin:6px 0 4px}
.services{background:var(--section-bg);height:618px;padding-top:41px}
.card{background:var(--card-bg);border:1px solid var(--card-border);padding:13px}
.card h3{font-weight:600;font-size:12.5px;line-height:16px;margin:0 0 8px}
.card p{margin-bottom:10px}
.wide{width:712px;margin:0 auto;height:218px}
.areas{display:grid;grid-template-columns:repeat(4,1fr);gap:0 16px;margin-top:2px}
.areas h4{font-weight:700;font-size:9.4px}
ul{padding-left:25px;list-style:disc}
ul ul{list-style:circle}
.row{width:712px;margin:15px auto 0;display:flex;gap:19px}
.row .card{width:225px;height:303px}
.site-footer{text-align:center;font-size:8px;line-height:15px;color:#555;padding-top:37px}
.site-footer a{color:var(--link);text-decoration:none}
.social{display:inline-block;width:8px;height:8px;background:var(--link);vertical-align:-1px;margin-left:2px}
</style>
</head>
<body>
<header class="site-header">
  <div class="brand"><span class="brand-mark"></span><span class="brand-name">Brivet Networks</span></div>
  <div class="tagline">Clear Steady Delivery</div>
  <nav class="main-nav">
    <a href="#">Home</a><a href="#">About us</a><a class="active" href="#">Services</a><a href="#">Strategy</a><a href="#">IT News</a><a href="#">Contact us</a>
  </nav>
</header>
<section class="hero">
  <h1>Our services</h1>
  <div class="inner">
    <h2>Leveraging People Process and Technology</h2>
    <p><strong>Brivet Networks, Inc.</strong> organizes our Services into four key areas. While these four services can be implemented individually the majority of our projects successfully combine componets from each. Our people and our process is what makes us successful in providing these services.</p>
  </div>
</section>
<section class="services">
  <div class="card wide">
    <h3>Professional Services</h3>
    <p>Our team provides experienced leadership and guidance, utilizing the industry standard methodologies. We help you maintain a comprehensive view of strategy, governance, technology, people and process, to deliver more successful business outcomes. Our expertise is focused in the following service areas.</p>
    <div class="areas">
      <div><h4>Virtualization</h4><ul><li>Cloud</li><li>Virtual Desktop Infrastructure (VDI)</li><li>Server Consolidation</li><li>Kelvra</li></ul></div>
      <div><h4>Messaging</h4><ul><li>Mailcore<ul><li>Implementation</li><li>Migration</li><li>Hosted Messaging</li></ul></li><li>Identity Directory Services<ul><li>Implementation</li><li>Migration</li></ul></li></ul></div>
      <div><h4>Security</h4><ul><li>Mobile Device Management (MDM)</li><li>Server Hardening</li></ul></div>
      <div><h4>Disaster Recovery/Business Continuity</h4><ul><li>Business Impact Analysis</li><li>Documentation</li><li>Implementation/Testing</li></ul></div>
    </div>
  </div>
  <div class="row">
    <div class="card">
      <h3>Hardware / Software Sales</h3>
      <p>We have access to multiple distributor partners throughout North America, as well as Elite Partner Status with many of the industry’s marquee manufacturers (such as Corvex) to ensure you are receiving the most aggressive pricing possible. Additionally, we have team members that possess the history, relationships and back office support to help simplify the process. By including procurement services in our total IT support offering, we simplify the IT implementation process while insuring your ability to get best pricing. We have the experience to recommend product solutions that will deliver the optimum in total cost of ownership.</p>
    </div>
    <div class="card">
      <h3>Technology Assessment</h3>
      <p>Experience has shown companies that perform objective, third-party technology assessments have proven to be instrumental in identifying weaknesses or breaches in their environments before they adversely impact their business.</p>
      <p>Our experts focus on the following key areas:</p>
      <ul><li>Network Assessment</li><li>Infrastructure Analysis</li><li>Health Checks</li><li>Performance Analysis</li></ul>
    </div>
    <div class="card">
      <h3>Technology Consulting</h3>
      <p>Implementing quality solutions is more than applying technology to problems. You need experts with deep technical knowledge and broad industry experience to help you design and implement cost-effective, reliable and secure solutions that meet your business priorities—on budget and on time. Our expertise focuses on the three key services below.</p>
      <p>Our experts focus on the following key areas:</p>
      <ul><li>Project Management<ul><li>CPM</li></ul></li><li>Business Improvement<ul><li>SMF</li></ul></li><li>Stafffing Solutions</li></ul>
    </div>
  </div>
</section>
<footer class="site-footer">
  <div>Copyright © 2019 Brivet Networks.</div>
  <div>Please see our <a href="#">policy</a> and feel free to <a href="#">contact us</a></div>
  <div>Follow us on <span class="social"></span><span class="social"></span></div>
</footer>
</body>
</html>
```